accomplished personal trainer, former elite gymnast from Russia, highly professional and experienced

Established Fitness trainer in California requires a new web site to attract personal clients and build her group exercise classes.

Here is an example of another fitness trainer's site that I really liked the technology:
http://www.tedmolvin.com

Below I have inserted my current web site: www.quorbalfitnesslodi.com
You can use this web site for the principal content, such as my background and qualifications.

Target Market(s)

Anyone who wants to improve their fitness levels and wellness in general. Anyone who needs directions and instruction on how to exercise. I can train anyone from elite athlete to a disabled person.

Industry/Entity Type

Fitness

Coding

Coded - Design and coding required

Number of Pages Required

5+ page

Font styles to use
Sans Serif

Requirements
Must have
• Easy to navigate main info about me, location, services, contact, benefits of using my services.
• Would be great to create unique representation of me as a trainer and a person, using new technologies and new ideas. Make it different from the other websites. Having its own character. Not too complicated and heavy with information, but an eye catching, useful and fun to navigate.
Nice to have
• new technology, easy access to information, the idea of enjoyment of life, lightness about achieving any goal, spiritual wisdom, unique design. I am planning to insert educational videos, advise, maybe jokes. Sign in, shopping cart, logo, should be easy for me to make changes in content.
Should not have
• cliché, outdated technology, too complicated,

```html
<!DOCTYPE html>
<html lang="en">
<head>
<meta charset="utf-8">
<title>Quorbal Fitness Lodi</title>
<link rel="stylesheet" href="https://fonts.googleapis.com/css2?family=Lato:wght@400;700;900&family=Dancing+Script:wght@700&family=Raleway:wght@400;500;700&display=swap">
<style>
:root{
  --green:#4cbf82;
  --green-dark:#2f9c63;
  --ink:#1e1e1e;
  --text:#2a2a2a;
  --muted:#9a9a9a;
  --about-bg:#f1f3f5;
  --consult-bg:#dcedf2;
  --line:#8ec9de;
  --footer:#262626;
  --white:#ffffff;
}
*{box-sizing:border-box;margin:0;padding:0}
html,body{width:1200px;height:3314px;overflow:hidden}
body{font-family:'Lato',sans-serif;color:var(--text);background:var(--white);position:relative}
section,header,footer{position:absolute;left:0;width:1200px}
.abs{position:absolute}

/* header + hero */
.hero{top:0;height:525px;background:linear-gradient(180deg,#5d6a4a 0%,#3f5234 40%,#2f4427 70%,#4d5c3a 100%)}
.site-header{top:0;height:90px;background:rgba(255,255,255,.88);z-index:2}
.brand{left:92px;top:26px;font-family:'Lato',sans-serif;font-weight:900;font-size:27px;color:var(--green);letter-spacing:.5px}
.main-nav{right:95px;top:38px;display:flex;gap:24px;list-style:none}
.main-nav li{font-size:12px;font-weight:700;color:var(--ink);letter-spacing:.3px}
.main-nav li.active{color:var(--green)}
.slider-dots{left:588px;top:490px;display:flex;gap:8px}
.slider-dots span{width:8px;height:8px;border-radius:50%;background:rgba(255,255,255,.5)}
.slider-dots span.on{background:#fff}

/* about */
.about{top:525px;height:564px;background:var(--about-bg)}
.script-title{font-family:'Dancing Script',cursive;font-weight:700}
.about h2{left:118px;top:86px;font-size:50px;color:var(--green)}
.about p{left:111px;top:168px;width:470px;font-size:16.5px;line-height:35px;color:var(--ink)}
.btn{display:flex;align-items:center;justify-content:center;background:var(--green);color:#fff;font-weight:700;font-size:19px;border-radius:6px;text-transform:uppercase}
.about .btn{left:111px;top:417px;width:218px;height:62px}
.about-shadow{left:560px;top:300px;width:560px;height:150px;border-radius:50%;background:radial-gradient(ellipse at center,#dde0e3 0%,rgba(241,243,245,0) 70%)}
.about-photo{left:690px;top:60px;width:410px;height:370px;border-radius:40% 40% 30% 30%;background:linear-gradient(180deg,#e8c9a6 0%,#2fa9c7 45%,#252b33 100%);opacity:.85}

/* consultation */
.consult{top:1089px;height:364px;background:var(--consult-bg);text-align:center}
.consult-figure{left:360px;top:20px;width:480px;height:340px;border-radius:50%;background:radial-gradient(ellipse at center,rgba(120,160,150,.25) 0%,rgba(220,237,242,0) 70%)}
.consult h2{left:0;width:1200px;top:56px;font-size:34px;color:var(--ink)}
.consult p{left:0;width:1200px;top:112px;font-size:12px;line-height:18px;color:var(--text)}
.field{height:47px;background:#fff;border-radius:3px;font-family:'Raleway',sans-serif;font-size:12px;color:#aaa;padding:16px 12px;text-align:left;top:180px}
.consult .btn{left:537px;top:253px;width:107px;height:40px;font-size:16px;border-radius:4px}

/* classes */
.classes{top:1453px;height:689px;background:#fff;text-align:center}
.section-title{left:0;width:1200px;font-weight:900;font-size:27px;color:var(--ink);text-transform:uppercase}
.section-sub{left:0;width:1200px;font-family:'Dancing Script',cursive;font-weight:700;font-size:19px;color:#777}
.classes .section-title{top:40px}
.classes .section-sub{top:96px}
.class-card{top:171px;width:322px}
.class-photo{width:322px;height:246px;border-radius:16px 16px 50% 50%/16px 16px 40px 40px;box-shadow:0 6px 8px rgba(0,0,0,.08)}
.class-card h3{margin-top:44px;font-size:15px;font-weight:700;color:var(--ink)}
.class-card time{display:block;margin-top:18px;font-family:'Raleway',sans-serif;font-size:13px;color:#555}
.class-card p{margin:16px auto 0;width:240px;font-family:'Raleway',sans-serif;font-size:12px;line-height:27px;color:var(--muted)}
.pager{top:620px;width:102px;height:34px;border:1px solid #ddd;border-radius:17px;display:flex;align-items:center;justify-content:center}

/* banner */
.banner{top:2142px;height:535px;background:linear-gradient(135deg,#6d7a44 0%,#3e5a2a 35%,#8aa05a 60%,#3a4d28 100%)}
.banner h2{left:102px;top:115px;font-family:'Lato',sans-serif;font-weight:700;font-size:60px;line-height:74px;color:var(--ink)}
.banner .btn{left:106px;top:339px;width:218px;height:59px}

/* blog */
.blog{top:2677px;height:483px;background:#fff;text-align:center}
.blog .section-title{top:46px}
.blog .section-sub{top:104px;font-size:17px}
.post{top:178px;display:flex;text-align:left}
.post-photo{width:235px;height:236px}
.post-body{margin-left:26px;width:220px}
.post-body h3{margin-top:12px;font-weight:700;font-size:22px;color:#555}
.post-body .rule{width:76px;height:3px;background:var(--line);margin-top:12px}
.post-body time{display:block;margin-top:10px;margin-left:8px;font-family:'Raleway',sans-serif;font-size:12px;color:#666}
.post-body p{margin-top:20px;font-family:'Raleway',sans-serif;font-size:12px;line-height:24px;color:var(--muted)}
.post-body .more{display:block;margin-top:14px;font-size:11px;font-weight:700;color:#666;letter-spacing:.5px}

/* footer */
.site-footer{top:3160px;height:154px;background:var(--footer);text-align:center;color:#fff}
.foot-nav{position:absolute;top:36px;left:0;width:1200px;display:flex;justify-content:center;gap:26px;list-style:none;font-size:12px;font-weight:700}
.copyright{position:absolute;top:68px;left:0;width:1200px;font-size:11px;color:#ddd}
.social{position:absolute;top:101px;left:0;width:1200px;display:flex;justify-content:center;gap:16px}
.social span{width:16px;height:16px;border-radius:50%;background:var(--green-dark)}
</style>
</head>
<body>

<section class="hero" role="img" aria-label="Photo of two women doing suspension strap stretches outdoors among trees">
  <div class="slider-dots abs"><span></span><span class="on"></span><span></span></div>
</section>

<header class="site-header">
  <div class="brand abs">QUORBAL FITNESS LODI</div>
  <ul class="main-nav abs">
    <li class="active">HOME</li>
    <li>ABOUT QUORBAL</li>
    <li>GROUP CLASSES</li>
    <li>PERSONAL TRAINING</li>
    <li>CONTACT</li>
    <li>BLOG</li>
  </ul>
</header>

<section class="about">
  <h2 class="script-title abs">About Me</h2>
  <p class="abs">Mira Solvanka is the owner of Quorbal Fitness. She grew up in the small town of Ostrevo, where she trained as a young athlete. Mira earned her degree from Kestrova Academy of Sport in Movement and Health Studies. For more than 20 years, Mira has worked as a dance teacher, balance mentor, and fitness trainer.</p>
  <div class="btn abs">Read More</div>
  <div class="about-shadow abs"></div>
  <div class="about-photo abs" role="img" aria-label="Photo of the trainer kneeling on the floor in a teal top and black leggings"></div>
</section>

<section class="consult">
  <div class="consult-figure abs" role="img" aria-label="Faint background photo of a woman stretching"></div>
  <h2 class="script-title abs">Need a Free consultation?</h2>
  <p class="abs">Lorem ipsum dolor sit amet, consectetur adipiscing elit, sed do eiusmod tempor<br>incididunt ut labore et dolore magna aliqua.</p>
  <div class="field abs" style="left:178px;width:262px">Name</div>
  <div class="field abs" style="left:454px;width:263px">Email</div>
  <div class="field abs" style="left:734px;width:263px">Phone</div>
  <div class="btn abs">Send</div>
</section>

<section class="classes">
  <h2 class="section-title abs">Our Classes</h2>
  <div class="section-sub abs">We will lead you from the beginner to a profession</div>

  <article class="class-card abs" style="left:92px">
    <div class="class-photo" role="img" aria-label="Photo of a group doing squats on a lawn" style="background:linear-gradient(180deg,#a9c98a 0%,#6aa34a 100%)"></div>
    <h3>FlowFit For Beginners</h3>
    <time>26/10/16 - 13:30 - 15:00</time>
    <p>Sed ut perspiciatis unde omnis iste natus error sit voluptatem accusantium.</p>
  </article>
  <article class="class-card abs" style="left:438px">
    <div class="class-photo" role="img" aria-label="Photo of two women in workout clothes in a park" style="background:linear-gradient(180deg,#8fb07a 0%,#4f7a3a 100%)"></div>
    <h3>FlowFit For Pregnant</h3>
    <time>28/08/16 - 9:30 - 10:30</time>
    <p>Sed ut perspiciatis unde omnis iste natus error sit voluptatem accusantium.</p>
  </article>
  <article class="class-card abs" style="left:786px">
    <div class="class-photo" role="img" aria-label="Photo of a group stretching side by side outdoors" style="background:linear-gradient(180deg,#9cc48a 0%,#5d9a3e 100%)"></div>
    <h3>Private &amp; Group Lessons</h3>
    <time>7/08/16 - 6:00 - 7:00</time>
    <p>Sed ut perspiciatis unde omnis iste natus error sit voluptatem accusantium.</p>
  </article>

  <div class="pager abs" style="left:499px"><svg width="12" height="12" viewBox="0 0 12 12"><path d="M8 1 3 6l5 5" fill="none" stroke="#999" stroke-width="1.6"/></svg></div>
  <div class="pager abs" style="left:613px"><svg width="12" height="12" viewBox="0 0 12 12"><path d="M4 1l5 5-5 5" fill="none" stroke="#999" stroke-width="1.6"/></svg></div>
</section>

<section class="banner" role="img" aria-label="Soft-focus photo of tree branches and green leaves">
  <h2 class="abs">Lorem ipsum dolor<br>ctetur adipiscing</h2>
  <div class="btn abs">Read More</div>
</section>

<section class="blog">
  <h2 class="section-title abs">Latest Blog</h2>
  <div class="section-sub abs">Newest from Fitness</div>

  <article class="post abs" style="left:92px">
    <div class="post-photo" role="img" aria-label="Photo of a woman hanging from a tree branch" style="background:linear-gradient(180deg,#7e9c5e 0%,#3c5a2e 100%)"></div>
    <div class="post-body">
      <h3>Vitality</h3>
      <div class="rule"></div>
      <time>2 Aug 2016</time>
      <p>Vivamus hendrerit arcu sed erat molestie vehicula. Sed auctor neque tellus rhoncus ut eleifend.</p>
      <span class="more">READ MORE</span>
    </div>
  </article>

  <article class="post abs" style="left:613px">
    <div class="post-photo" role="img" aria-label="Photo of two women training with an exercise ball on grass" style="background:linear-gradient(180deg,#9fbf7e 0%,#5e8d42 100%)"></div>
    <div class="post-body">
      <h3>Sweet Cakes</h3>
      <div class="rule"></div>
      <time>2 Aug 2016</time>
      <p>Working from home meant we could vary snack and coffee breaks, change our desks.</p>
      <span class="more">READ MORE</span>
    </div>
  </article>
</section>

<footer class="site-footer">
  <ul class="foot-nav">
    <li>HOME</li><li>ABOUT QUORBAL</li><li>GROUP CLASSES</li><li>PERSONAL TRAINING</li><li>CONTACT</li><li>BLOG</li>
  </ul>
  <div class="copyright">Copyright © 2016 . All Rights Reserved</div>
  <div class="social"><span></span><span></span><span></span><span></span><span></span><span></span></div>
</footer>

</body>
</html>
```